A new medical waste company needs an attractive and modern flyer.

We are a new medical waste company disposing of biohazards waste, red bag waste and sharps disposal with a focus on customer service.

Background Information

Company Name
Trovik Waste

Industry
Medical waste management

Description of the organization and its target audience

We are a new medical waste company disposing of biohazardous waste, red bag waste and medical sharps.

Description

MODERN & ELEGANT HALF PAGE FLYER

Half page mailer (front and back) with a large image related to the medical field.

The Trovik Waste logo, with the company tag line “compliant waste solutions” should also be on front of the mailer.

Website (trovikwaste.com) & email (info@trovikwatse.com) on both sides of the flyer

Main headline
-Now you have options for your medical waste disposal

Who we serve
- Dentist
- Physicians
-Blood banks
-Tattoo parlors
-Assisted living facilities
-Laboratories
-Veterinarians

What we offer
-Straight forward pricing
-No hidden fees
-No long term contracts
-Free containers and red bags
-Routine scheduled pickups

Price $35.95
Updates

Remember this is a half page flyer. Please remove pricing from all future work.

Target Market(s)

- Dentist
- Physicians
-Blood banks
-Tattoo parlors
-Laboratories
-Veterinarians

Industry/Entity Type

It Company

Colors
33b8a4

Requirements
Must have
• See my website www.trovikwaste.com

```html
<!DOCTYPE html>
<html lang="en">
<head>
<meta charset="utf-8">
<title>Trovik Waste – Medical Waste Flyer</title>
<link rel="stylesheet" href="https://fonts.googleapis.com/css2?family=Questrial&family=Montserrat:wght@600&display=swap">
<style>
  :root {
    --teal: #33b8a4;
    --teal-deep: #16957f;
    --teal-dark: #0f7f6b;
    --teal-ink: #137a68;
    --logo-green: #3f8a4a;
    --ink: #2b2b2b;
    --white: #ffffff;
    --mint-text: #e4f7f2;
  }
  * { margin: 0; padding: 0; box-sizing: border-box; }
  html, body { width: 846px; height: 1200px; overflow: hidden; background: var(--white); }
  body { font-family: "Questrial", sans-serif; }
  .flyer { position: relative; width: 846px; height: 1200px; overflow: hidden; }
  .backdrop { position: absolute; inset: 0; }

  .headline-band {
    position: absolute; top: 0; left: 0; width: 846px; height: 66px;
    background: var(--teal-ink); color: var(--white);
    font-size: 28px; line-height: 70px; padding-left: 28px; white-space: nowrap;
  }
  .intro {
    position: absolute; top: 74px; left: 32px; width: 790px;
    font-size: 19.6px; line-height: 32px; color: var(--ink);
  }

  .audience { position: absolute; left: 50px; top: 608px; color: var(--white); }
  .audience h2 { font-weight: 400; font-size: 30px; margin-bottom: 12px; }
  .audience ul { list-style: none; }
  .audience li { position: relative; font-size: 24px; line-height: 38px; padding-left: 38px; }
  .audience li::before {
    content: ""; position: absolute; left: 2px; top: 13px;
    width: 12px; height: 12px; border-radius: 50%; background: var(--white);
  }

  .benefits {
    position: absolute; left: 468px; top: 566px; width: 440px;
    transform: rotate(-5deg); transform-origin: left top;
  }
  .benefits li {
    list-style: none; height: 50px; margin-bottom: 8px;
    background: var(--teal-dark); color: var(--white);
    font-size: 26px; line-height: 54px; padding-left: 24px; white-space: nowrap;
  }
  .benefits li:nth-child(odd) { background: var(--teal-ink); }

  .brand-panel {
    position: absolute; left: 0; top: 950px; width: 456px; height: 152px;
    background: var(--white); display: flex; align-items: center; padding-left: 30px; gap: 22px;
  }
  .brand-dot { width: 22px; height: 22px; border-radius: 50%; background: var(--logo-green); flex: none; }
  .brand-name { font-size: 42px; color: #1a1a1a; letter-spacing: 2px; white-space: nowrap; }

  .tagline {
    position: absolute; left: 30px; top: 1104px; color: var(--white);
    font-size: 29px; line-height: 48px;
  }

  .contact {
    position: absolute; left: 450px; top: 1008px; width: 400px; text-align: center;
    color: var(--mint-text); font-size: 23px; line-height: 32px; font-style: normal;
  }

  .website {
    position: absolute; left: 478px; top: 1124px; width: 346px; text-align: right;
    font-family: "Montserrat", sans-serif; font-weight: 600; font-size: 35px;
    line-height: 56px; color: var(--teal-ink); white-space: nowrap;
  }
</style>
</head>
<body>
<main class="flyer">
  <svg class="backdrop" width="846" height="1200" viewBox="0 0 846 1200">
    <defs>
      <linearGradient id="photoTone" x1="0" y1="0" x2="1" y2="1">
        <stop offset="0" stop-color="#c9cfce"/>
        <stop offset="0.55" stop-color="#a9b0ae"/>
        <stop offset="1" stop-color="#e2e5e3"/>
      </linearGradient>
    </defs>
    <rect x="0" y="180" width="846" height="1020" fill="var(--teal)"/>
    <polygon points="0,1160 846,1060 846,1200 0,1200" fill="var(--teal-deep)"/>
    <polygon points="560,900 846,860 846,1200 520,1200" fill="var(--teal-deep)"/>
    <polygon points="0,1102 416,1102 376,1156 0,1156" fill="var(--teal-dark)"/>
    <polygon points="478,1124 846,1124 846,1180 440,1180" fill="var(--white)"/>
    <rect x="0" y="1180" width="846" height="20" fill="var(--teal-dark)"/>
    <polygon role="img" aria-label="Photo of a worker in protective clothing and gloves carrying a yellow biohazard waste bag across a clean facility floor"
             points="0,180 846,180 846,496 0,600" fill="url(#photoTone)"/>
  </svg>

  <header class="headline-band">Now you have options for your medical waste disposal</header>
  <p class="intro">From collection to disposal, Trovik Waste is a provider of cost effective medical waste disposal in Kentuckiana and Southern Indiana. Maintain compliance with qualified collection, transport, and disposal of sharps and bio hazardous waste.</p>

  <section class="audience">
    <h2>Who we serve</h2>
    <ul>
      <li>Dentist</li>
      <li>Physicians</li>
      <li>Veterinarians</li>
      <li>Blood banks</li>
      <li>Laboratories</li>
      <li>Tattoo parlors</li>
      <li>Assisted living facilities</li>
    </ul>
  </section>

  <ul class="benefits">
    <li>Straight Forward Pricing</li>
    <li>No Hidden Fees</li>
    <li>No Long Term Contracts</li>
    <li>Free Containers &amp; Bags</li>
    <li>Routine Scheduled Pickups</li>
  </ul>

  <div class="brand-panel">
    <span class="brand-dot"></span>
    <span class="brand-name">TROVIK WASTE</span>
  </div>
  <p class="tagline">compliant waste solutions</p>

  <address class="contact">
    For More Details<br>
    Call us : 000 000 0000 or<br>
    Mail us : info@trovikwatse.com
  </address>

  <div class="website">trovikwaste.com</div>
</main>
</body>
</html>
```